Webshop for furniture and lamps

We need a design for a web shop with APP that should have two options:
1-Webshop in general which should attract to private customer in general and
2-Website that is meant to attract big customers as hotels and restaurants who would have their own customerize login.

That's the idea behind the shop.

It should be diveded into 4 parts
vintage furniture
rattan set outdoor and indoor
lamps and
wooden wall decor

The name of the shop is brisa novelta!

Please kindly make me an offer.

Reason: Dear designers, so far there hasn't been a design that really matched. Look up German web sites like www.fernblick-art.de or www.holzkante17.de... Haven't been convinced by designs! Sorry folks. Please submit some new ones. Kind regards Ned

```html
<!DOCTYPE html>
<html lang="en">
<head>
<meta charset="utf-8">
<title>Brisa Novelta — Furniture &amp; Lamps</title>
<link href="https://fonts.googleapis.com/css2?family=Cabin:wght@400;500;600&family=Libre+Baskerville:wght@700&family=Open+Sans:wght@400&display=swap" rel="stylesheet">
<style>
  :root {
    --gold-top: #e3b41c;
    --gold-bottom: #c47e0a;
    --nav-brown: #b1660c;
    --nav-divider: #c98a3a;
    --accent: #c2780a;
    --accent-dark: #9a5a0c;
    --tick: #e39a12;
    --ink: #2d2d2d;
    --body-text: #6f6f6f;
    --card-border: #e2e2e2;
    --footer-bg: #271d10;
    --footer-muted: #8a8478;
    --white: #ffffff;
  }
  * { margin: 0; padding: 0; box-sizing: border-box; }
  html, body { width: 1131px; height: 1200px; overflow: hidden; }
  body {
    position: relative;
    font-family: "Cabin", sans-serif;
    color: var(--ink);
    background: linear-gradient(180deg, #dcdcdc 146px, #f2f2f2 380px, #ffffff 530px);
  }
  .site-header {
    position: absolute; left: 0; top: 0; width: 1131px; height: 146px;
    background: linear-gradient(180deg, var(--gold-top), var(--gold-bottom));
  }
  .brand {
    position: absolute; left: 146px; top: 36px;
    font-family: "Libre Baskerville", serif; font-weight: 700;
    font-size: 33px; color: var(--white); letter-spacing: 0.5px;
  }
  .phone {
    position: absolute; right: 141px; top: 56px;
    display: flex; align-items: center; gap: 5px;
    font-size: 21px; color: var(--white);
  }
  .main-nav {
    position: absolute; left: 144px; top: 99px; width: 843px; height: 47px;
    background: var(--nav-brown); display: flex;
  }
  .main-nav a {
    flex: auto; display: flex; align-items: center; justify-content: center;
    color: var(--white); text-decoration: none; font-size: 15px;
    border-right: 1px solid var(--nav-divider);
  }
  .main-nav a:last-child { border-right: none; }
  .hero {
    position: absolute; left: 144px; top: 146px; width: 843px; height: 381px;
    background: linear-gradient(180deg, #9fb56e 0%, #8a9a4a 28%, #c79b58 40%, #84725a 58%, #7b6a55 80%, #a49a8c 100%);
  }
  .hero-dots {
    position: absolute; left: 393px; top: 358px; display: flex; gap: 5px;
  }
  .hero-dots span { width: 10px; height: 10px; border-radius: 50%; background: #f2f2f2; }
  .about {
    position: absolute; left: 144px; top: 560px; width: 277px;
  }
  .section-title { font-size: 23px; font-weight: 400; color: var(--ink); }
  .about p {
    font-family: "Open Sans", sans-serif; font-size: 10.6px; line-height: 18px;
    color: var(--body-text); margin-top: 5px; padding-left: 1px;
  }
  .about .section-title { margin-bottom: 8px; }
  .promo {
    position: absolute; left: 430px; top: 550px; width: 268px; height: 167px;
    background: linear-gradient(90deg, #6a6762 0%, #8c7a68 30%, #a07c5c 60%, #c19b74 100%);
  }
  .promo-band {
    position: absolute; left: 0; bottom: 0; width: 100%; height: 45px;
    background: rgba(205, 140, 30, 0.88);
    display: flex; align-items: center; padding-left: 16px;
    color: var(--white); font-size: 19px;
  }
  .promo-arrow {
    position: absolute; right: 0; top: 0; width: 45px; height: 45px;
    border-radius: 22px 0 0 22px; background: rgba(160, 95, 10, 0.6);
    display: flex; align-items: center; justify-content: center;
  }
  .services {
    position: absolute; left: 712px; top: 550px; width: 273px; height: 167px;
    border: 1px solid #e6e6e6;
    background: linear-gradient(180deg, #ffffff 60%, #f3f3f3);
    padding: 18px 0 0 27px;
  }
  .services h2 { font-size: 19px; font-weight: 400; color: var(--accent-dark); margin-bottom: 10px; }
  .services ul { list-style: none; }
  .services li {
    display: flex; align-items: center; gap: 7px;
    font-size: 12.5px; color: var(--ink); height: 23.5px;
  }
  .divider { position: absolute; left: 145px; top: 742px; width: 843px; height: 1px; background: #e8e8e8; }
  .products-title { position: absolute; left: 144px; top: 775px; font-size: 22px; }
  .product-grid { position: absolute; left: 145px; top: 816px; display: flex; gap: 8px; }
  .product-card {
    width: 205px; height: 218px; border: 1px solid var(--card-border);
    background: var(--white); padding: 12px 12px 0 12px;
  }
  .product-photo { width: 180px; height: 118px; border: 1px solid #e6e6e6; }
  .product-name { margin: 13px 0 0 5px; font-size: 15px; font-weight: 400; color: var(--accent); }
  .product-card p {
    margin: 4px 0 0 5px; font-family: "Open Sans", sans-serif;
    font-size: 10.6px; line-height: 18px; color: var(--body-text);
  }
  .site-footer {
    position: absolute; left: 0; top: 1086px; width: 1131px; height: 114px;
    background: var(--footer-bg);
  }
  .footer-nav {
    position: absolute; left: 145px; top: 33px;
    font-size: 13.8px; font-weight: 600; color: var(--white);
  }
  .footer-nav a { color: var(--white); text-decoration: none; }
  .footer-nav .sep { margin: 0 5px; }
  .copyright {
    position: absolute; left: 145px; top: 58px;
    font-family: "Open Sans", sans-serif; font-size: 10.5px; color: var(--footer-muted);
  }
  .social { position: absolute; left: 892px; top: 47px; display: flex; gap: 4px; }
  .social span { width: 26px; height: 26px; border-radius: 50%; background: var(--white); }
</style>
</head>
<body>
  <header class="site-header">
    <div class="brand">Brisa Novelta</div>
    <div class="phone">
      <svg width="24" height="24" viewBox="0 0 24 24" aria-hidden="true">
        <circle cx="12" cy="12" r="10.5" fill="none" stroke="#fff" stroke-width="1.8"/>
        <path d="M8.6 6.8c.5-.4 1.1-.3 1.4.2l1 1.6c.3.5.2 1-.2 1.3l-.6.5c.5 1.3 1.5 2.4 2.8 3l.5-.6c.3-.4.9-.5 1.3-.2l1.6 1c.5.3.6.9.2 1.4l-.7.8c-.6.6-1.6.8-2.4.4-2.6-1.2-4.6-3.3-5.7-5.9-.3-.8-.1-1.7.5-2.3z" fill="#fff"/>
      </svg>
      555.204.7731
    </div>
    <nav class="main-nav">
      <a href="#">Home</a><a href="#">About Us</a><a href="#">Our Funiture</a><a href="#">Why Choose Us</a><a href="#">Services Provide</a><a href="#">Order Now</a><a href="#">Contact Us</a>
    </nav>
  </header>

  <div class="hero" role="img" aria-label="Rattan lounge set with sofa, armchair and round table on a wooden deck, garden trees behind">
    <div class="hero-dots"><span></span><span></span><span></span><span></span></div>
  </div>

  <section class="about">
    <h2 class="section-title">About Our Company</h2>
    <p>Mauris vel lacus vitae felis vestibulum volutpat Etiam est nunc venenatis in tristique eu imperdiet ac nisl Cum sociis natoque penatibus et magnis dis parturient montes nascetur ridiculus mus In iaculis</p>
    <p>Facilisis massa Etiam eu urna Sed porta Suspendisse quam leo molestie sed luctus quis feugi</p>
  </section>

  <a class="promo" href="#" role="img" aria-label="Bedroom interior with a wooden mosaic wall and a bed">
    <span class="promo-band">Buy Our Furniture
      <span class="promo-arrow">
        <svg width="14" height="24" viewBox="0 0 14 24" aria-hidden="true"><path d="M2 2l10 10L2 22" fill="none" stroke="#fff" stroke-width="2"/></svg>
      </span>
    </span>
  </a>

  <aside class="services">
    <h2>Services We Provide</h2>
    <ul>
      <li><svg width="12" height="10" viewBox="0 0 12 10" aria-hidden="true"><path d="M1 5.5l3.3 3L11 1.5" fill="none" stroke="#e39a12" stroke-width="2.4"/></svg>Vintage furniture</li>
      <li><svg width="12" height="10" viewBox="0 0 12 10" aria-hidden="true"><path d="M1 5.5l3.3 3L11 1.5" fill="none" stroke="#e39a12" stroke-width="2.4"/></svg>Rattan set outdoor and indoor</li>
      <li><svg width="12" height="10" viewBox="0 0 12 10" aria-hidden="true"><path d="M1 5.5l3.3 3L11 1.5" fill="none" stroke="#e39a12" stroke-width="2.4"/></svg>Lamps</li>
      <li><svg width="12" height="10" viewBox="0 0 12 10" aria-hidden="true"><path d="M1 5.5l3.3 3L11 1.5" fill="none" stroke="#e39a12" stroke-width="2.4"/></svg>Wooden wall decor</li>
    </ul>
  </aside>

  <div class="divider"></div>

  <h2 class="section-title products-title">Latest Products</h2>
  <div class="product-grid">
    <article class="product-card">
      <div class="product-photo" role="img" aria-label="Vintage wooden cabinet with painted tile drawers" style="background: linear-gradient(90deg,#e6e2dc,#6b4a32 30%,#5a3c28 70%,#d8d2ca);"></div>
      <h3 class="product-name">Product Name</h3>
      <p>Etiam est nunc venenatis in tris-<br>tique eu imperdiet ac nisl</p>
    </article>
    <article class="product-card">
      <div class="product-photo" role="img" aria-label="Floor lamp with a red shade" style="background: linear-gradient(180deg,#ffffff,#fbf7f5);"></div>
      <h3 class="product-name">Product Name</h3>
      <p>Etiam est nunc venenatis in tris-<br>tique eu imperdiet ac nisl</p>
    </article>
    <article class="product-card">
      <div class="product-photo" role="img" aria-label="Painted wooden wall decor panel" style="background: linear-gradient(90deg,#3d6a5a,#5a6b62 45%,#b8b2a8 70%,#ddd8cf);"></div>
      <h3 class="product-name">Product Name</h3>
      <p>Etiam est nunc venenatis in tris-<br>tique eu imperdiet ac nisl</p>
    </article>
    <article class="product-card">
      <div class="product-photo" role="img" aria-label="Round rattan dining set with tucked-in chairs" style="background: radial-gradient(ellipse at 55% 55%,#5a5a5c 0%,#707073 35%,#ffffff 62%);"></div>
      <h3 class="product-name">Product Name</h3>
      <p>Etiam est nunc venenatis in tris-<br>tique eu imperdiet ac nisl</p>
    </article>
  </div>

  <footer class="site-footer">
    <nav class="footer-nav">
      <a href="#">Home</a><span class="sep">|</span><a href="#">About Us</a><span class="sep">|</span><a href="#">Our Funiture</a><span class="sep">|</span><a href="#">Why Choose Us</a><span class="sep">|</span><a href="#">Services Provide</a><span class="sep">|</span><a href="#">Order Now</a><span class="sep">|</span><a href="#">Contact Us</a>
    </nav>
    <div class="copyright">© 2014 Company Name &nbsp;All right reserved &nbsp;Term of Use</div>
    <div class="social" aria-label="Social links"><span></span><span></span><span></span></div>
  </footer>
</body>
</html>
```